Professional Services - letterhead / business cards

The company (velmora holdings) will provide services to Investment Funds and large investors in Spain. I have recently chosen a logo that I am attaching.

I would like a simple stationary design that i could use as letter head, business cards and "with compliments" cards.

I am not quite sure which color I will mostly use for the logo, in the email signature I will probably lean towards the white background and grey letters. I am attaching my favourite options.

Target Market(s)

Large Multinationals, Investment funds and Law firms

Industry/Entity Type

Business

Requirements
Must have
• my details are:
Luis R. Albarda
Velmora Holdings S.L.
Casa de Valdetorres
Calle de Ortuzar Beltrán 27
28019 Madrid
T: +34 (91) 387-6051
M: +34 (655) 814-073
e-mail: lalbarda@velmoraholdings.example

```html
<!DOCTYPE html>
<html lang="en">
<head>
<meta charset="utf-8">
<title>Velmora Holdings – Stationery</title>
<link href="https://fonts.googleapis.com/css2?family=PT+Sans:wght@400;700&display=swap" rel="stylesheet">
<style>
  :root {
    --backdrop-top: #fbfcfd;
    --backdrop-bottom: #e6f1f6;
    --paper: #ffffff;
    --charcoal: #555457;
    --slate: #706d6e;
    --stone: #8f8b8b;
    --mist: #d9d9da;
    --ink: #1e1e1e;
    --shadow: rgba(0,0,0,.45);
  }
  * { box-sizing: border-box; margin: 0; padding: 0; }
  html, body { width: 1200px; height: 818px; overflow: hidden; }
  body {
    font-family: "PT Sans", sans-serif;
    color: var(--ink);
    background: linear-gradient(180deg, var(--backdrop-top), var(--backdrop-bottom));
    position: relative;
  }
  .sheet { position: absolute; background: var(--paper); box-shadow: 3px 4px 5px var(--shadow); overflow: hidden; }
  .wordmark { font-family: "PT Sans", sans-serif; font-weight: 400; color: #fff; white-space: nowrap; position: absolute; letter-spacing: .2px; }

  /* Letterhead */
  .letterhead { left: 120px; top: 101px; width: 461px; height: 648px; }
  .letterhead__topbar { position: absolute; left: 0; top: 0; width: 100%; height: 11px; background: linear-gradient(90deg, var(--mist), var(--stone) 70%, var(--charcoal)); }
  .letterhead__sender { position: absolute; left: 304px; top: 24px; font-size: 11px; line-height: 13px; }
  .letterhead__footer { position: absolute; left: 0; top: 600px; width: 100%; height: 33px; background: var(--charcoal); }
  .letterhead__footer .wordmark { right: 22px; top: 8px; font-size: 14px; }
  .letterhead__strip { position: absolute; left: 0; top: 633px; width: 100%; height: 15px; background: linear-gradient(90deg, var(--mist), var(--stone)); }

  /* Compliments slip */
  .slip { left: 632px; top: 132px; width: 483px; height: 254px; }
  .slip__panel { position: absolute; right: 0; top: 0; width: 139px; height: 220px; background: var(--stone); }
  .slip__strip { position: absolute; left: 0; top: 220px; width: 100%; height: 34px; background: linear-gradient(90deg, var(--mist), var(--stone) 65%, var(--slate)); }
  .slip__strip .wordmark { right: 14px; top: 8px; font-size: 16px; }
  .slip__details { position: absolute; left: 33px; top: 165px; display: flex; gap: 55px; font-size: 9px; line-height: 11px; }
  .name { font-weight: 700; }

  /* Business cards */
  .card { position: absolute; border-radius: 10px; overflow: hidden; box-shadow: 3px 4px 5px var(--shadow); }
  .card--front { left: 673px; top: 466px; width: 183px; height: 122px; background: var(--slate); }
  .card--front .card__sheen { position: absolute; left: 0; top: 0; width: 100%; height: 44px; background: linear-gradient(180deg, #f2f2f2, var(--mist)); }
  .card--front .card__band { position: absolute; left: 0; top: 44px; width: 100%; height: 37px; background: var(--charcoal); }
  .card--front .wordmark { left: 12px; top: 9px; font-size: 15px; }

  .card--back { left: 874px; top: 426px; width: 183px; height: 124px; background: linear-gradient(180deg, #f5f5f5, var(--mist) 55%, #c3c3c4); }
  .card--back .card__cap { position: absolute; left: 0; top: 0; width: 100%; height: 11px; background: var(--charcoal); }
  .card--back .card__base { position: absolute; left: 0; bottom: 0; width: 100%; height: 10px; background: var(--charcoal); }
  .card--back .card__rule { position: absolute; left: 108px; top: 36px; width: 1px; height: 46px; background: var(--charcoal); }
  .card--back .card__who { position: absolute; left: 10px; top: 42px; font-size: 6px; line-height: 7.4px; }
  .card--back .card__lines { position: absolute; left: 113px; top: 64px; font-size: 6px; line-height: 7.4px; }
  .card--back .wordmark { color: var(--charcoal); left: 44px; top: 95px; font-size: 12px; }
</style>
</head>
<body>
  <section class="sheet letterhead" aria-label="Letterhead">
    <div class="letterhead__topbar"></div>
    <address class="letterhead__sender" style="font-style:normal">
      <div class="name">Luis R. Albarda</div>
      <div>Velmora Holdings S.L.</div>
      <div>Calle de Ortuzar Beltrán 27</div>
      <div>28019 Madrid</div>
    </address>
    <div class="letterhead__footer"><span class="wordmark">velmora holdings</span></div>
    <div class="letterhead__strip"></div>
  </section>

  <section class="sheet slip" aria-label="With compliments slip">
    <div class="slip__panel"></div>
    <div class="slip__details">
      <address style="font-style:normal">
        <div class="name">Luis R. Albarda</div>
        <div>Velmora Holdings S.L.</div>
        <div>Calle de Ortuzar Beltrán 27</div>
        <div>28019 Madrid</div>
      </address>
      <div>
        <div>&nbsp;</div>
        <div>T: +34 (91) 387-6051</div>
        <div>M: +34 (655) 814-073</div>
        <div>lalbarda@velmoraholdings.example</div>
      </div>
    </div>
    <div class="slip__strip"><span class="wordmark">velmora holdings</span></div>
  </section>

  <section class="card card--front" aria-label="Business card front">
    <div class="card__sheen"></div>
    <div class="card__band"><span class="wordmark">velmora holdings</span></div>
  </section>

  <section class="card card--back" aria-label="Business card back">
    <div class="card__cap"></div>
    <address class="card__who" style="font-style:normal">
      <div class="name">Luis R. Albarda</div>
      <div>Velmora Holdings S.L.</div>
      <div>Calle de Ortuzar Beltrán 27</div>
      <div>28019 Madrid</div>
      <div>lalbarda@velmoraholdings.example</div>
    </address>
    <div class="card__rule"></div>
    <div class="card__lines">
      <div>T: +34 (91) 387-6051</div>
      <div>M: +34 (655) 814-073</div>
    </div>
    <span class="wordmark">velmora holdings</span>
    <div class="card__base"></div>
  </section>
</body>
</html>
```